Professional, polished website design for boutique wealth management firm

Hello, thank you for your interest. PLEASE READ THE BRIEF BEFORE SUBMITTING THE DESIGN.-
PLEASE USE THE ATTACHED HOME PAGE COPY FOR THIS DESIGN.
We are looking for a professional, polished design that helps portray trust and credibility for a well-established independent wealth management firm. We have copy we've written for the home page and we'd like the design and imagery to play up the copy, so there's a better chance someone will read it all. So the headlines etc should all be easy to read and the design should draw the eye towards them. For colors, again trust is important so probably blue as a dominant color, but you can also use gray, green, etc. We'd like to avoid too much use of the color red (due to financial, association with loss). SO PLEASE AVOID USE OF THE COLOR RED. We also like bright orange or yellow for call to action buttons.

Please keep the design EASY TO MAINTAIN in wordpress as well.

I have attached home page copy as well as logo files.

Here's some sites that we like so feel free to use as inspiration:
https://www.brovaltcapitalworks.example/, https://harborpathpensionsplains.example/
https://tavrin-oakes.example/, https://plantfornextyear.example/, https://ferngatefinancial.example/

As another option/idea, I like the idea of a simple format with a clean image similar to this for the home page: https://www.pixmeadowstock.example/detail/photo/calculator-falling-royalty-free-image/31684207?adppopup=true
Just an idea.

Also please be sure to incorporate the QWA /Accredited Wealth Steward logo as well, farther down the page is fine.

Thank you for your help! Feel free to contact me with any questions.

Target Market(s)

Individuals aged 48-62 who are looking to maximize their wealth, such as business owners, executives, engineers, successful tradespeople, etc.

Industry/Entity Type

Finance--wealth management

Font styles to use
Sans Serif

Requirements
Must have
• Professional and polished, Call to action buttons must be clear and stand out, headlines must be clear and stand out, also text must be big enough to be easily readable by most people
Should not have
• Anything casual, frilly, etc.

```html
<!DOCTYPE html>
<html lang="en">
<head>
<meta charset="utf-8">
<title>Sentinel Ridge Advisors</title>
<link rel="stylesheet" href="https://fonts.googleapis.com/css2?family=Outfit:wght@300;400;500;600;700&family=Libre+Caslon+Text:wght@400;700&display=swap">
<style>
:root{
  --brand:#3b46a6;
  --brand-deep:#2c3794;
  --navy:#1b2463;
  --ink:#1c2340;
  --text:#3b3f52;
  --muted:#8a8fa3;
  --cta:#fdb515;
  --tint:#f4f5fb;
  --card:#f6f6f8;
  --line:#d9dbe4;
  --green:#7cc24a;
  --white:#ffffff;
}
*{box-sizing:border-box;margin:0;padding:0}
html,body{width:1200px;height:3881px;overflow:hidden}
body{position:relative;font-family:"Outfit",sans-serif;color:var(--text);background:var(--white)}
.abs{position:absolute}
.serif{font-family:"Libre Caslon Text",serif}

/* hero */
.hero{left:0;top:0;width:1200px;height:629px;background:linear-gradient(100deg,#3a45a8 0%,#3c48ab 55%,#34409e 100%)}
.brand{display:flex;align-items:center;gap:10px;color:var(--white)}
.brand-dot{width:44px;height:44px;border-radius:50%;background:rgba(255,255,255,.22)}
.brand-name{font-family:"Libre Caslon Text",serif;font-size:26px;line-height:1;letter-spacing:1px}
.brand-sub{font-size:14px;letter-spacing:.5px}
.nav{left:460px;top:44px;display:flex;gap:20px;font-family:"Libre Caslon Text",serif;font-size:12px;color:var(--white);letter-spacing:.3px}
.btn-outline-light{left:796px;top:33px;width:122px;height:36px;border:1.5px solid var(--white);border-radius:18px;color:var(--white);font-family:"Libre Caslon Text",serif;font-size:11.5px;display:flex;align-items:center;justify-content:center}
.btn-cta{background:var(--cta);color:var(--white);border-radius:24px;display:flex;align-items:center;justify-content:center;font-family:"Libre Caslon Text",serif}
.quote-btn{left:929px;top:33px;width:151px;height:36px;font-size:11.5px;font-weight:700}
.hero-title{left:139px;top:222px;color:var(--white);font-family:"Libre Caslon Text",serif;line-height:1.25}
.hero-title .l1{font-size:30px;display:block}
.hero-title .l2{font-size:44px;font-weight:700;display:block;margin:2px 0}
.hero-title .l3{font-size:30px;display:block}
.hero-learn{left:139px;top:397px;width:160px;height:45px;font-size:16px}
.hero-photo{left:692px;top:116px;width:388px;height:442px;border-radius:12px;background:linear-gradient(150deg,#c7c9cf 0%,#8e8f94 45%,#5a4a3e 80%,#d7d8dc 100%)}

/* intro */
.ghost-circle{border-radius:50%;background:var(--tint)}
.h2{font-size:26px;font-weight:500;color:var(--ink);line-height:1.32}
.body{font-size:13px;line-height:1.6;color:var(--text)}
.btn-outline{border:1.5px solid #999;border-radius:20px;font-size:13px;font-weight:500;color:var(--ink);display:flex;align-items:center;justify-content:center}
.btn-solid{background:var(--brand-deep);color:var(--white);border-radius:20px;font-size:13px;font-weight:500;display:flex;align-items:center;justify-content:center}
.emblem{border-radius:50%;background:linear-gradient(160deg,#5560c2,#2c3794)}

.photo-calc{left:234px;top:1151px;width:301px;height:298px;border-radius:10px;background:linear-gradient(150deg,#b9bbc1 0%,#85868b 50%,#524437 85%,#d4d5d9 100%)}

/* promise band */
.band{left:0;top:1550px;width:1200px;height:314px;background:var(--tint)}
.band-lead{left:0;top:1670px;width:1200px;text-align:center;font-size:30px;font-weight:300;color:var(--ink)}
.band-strong{left:0;top:1715px;width:1200px;text-align:center;font-size:31px;font-weight:600;color:var(--brand-deep)}
.band-note{left:0;top:1771px;width:1200px;text-align:center;font-size:14px;color:var(--ink)}
.band-arrow{left:560px;top:1818px;width:80px;height:80px;border-radius:50%;background:var(--tint);display:flex;align-items:center;justify-content:center}

/* services */
.svc{background:var(--card);border:1px solid #eceef2;border-radius:4px;display:flex;flex-direction:column;align-items:center;justify-content:center;gap:12px;text-align:center;font-size:17px;font-weight:500;color:var(--ink);line-height:1.2}
.svc.active{background:var(--brand-deep);color:var(--white);border-color:var(--brand-deep)}
.svc svg{width:54px;height:54px}
.svc-heading{left:712px;top:1948px;font-size:33px;line-height:1.3;color:var(--ink);font-weight:400}
.svc-heading strong{font-weight:700;font-size:38px}

/* check-up */
.checkup-photo{left:382px;top:2544px;width:624px;height:415px;background:linear-gradient(120deg,#7f87c8 0%,#c9cbe6 45%,#e7e2ec 70%,#b8a6c6 100%)}
.checkup-card{left:193px;top:2563px;width:427px;height:378px}
.checkup-title{left:258px;top:2632px;font-size:23px;font-weight:500;color:var(--ink);line-height:1.45}
.checkup-text{left:258px;top:2712px;width:300px;font-size:10.5px;line-height:1.62;color:var(--ink)}

/* contact */
.contact-title{left:0;top:3110px;width:1200px;text-align:center;font-size:34px;font-weight:700;color:#222;letter-spacing:.5px}
.contact-lead{left:0;top:3156px;width:1200px;text-align:center;font-size:14px;line-height:1.5;color:#444}
.footer-bg{left:0;top:3393px;width:1200px;height:488px;background:linear-gradient(180deg,#1f2a70 0%,#1a2360 60%,#1d2768 100%)}
.form-card{left:193px;top:3220px;width:813px;height:301px;background:var(--white);border-top:3px solid var(--green);box-shadow:0 4px 18px rgba(20,30,80,.1)}
.form-title{left:283px;top:3247px;font-size:19px;color:#333}
.field{border:1px solid var(--line);border-radius:2px;font-size:10px;color:#999;padding:8px 14px;background:var(--white)}
.submit{left:283px;top:3459px;width:117px;height:30px;background:var(--brand-deep);color:var(--white);font-size:12px;font-weight:600;display:flex;align-items:center;justify-content:center;border-radius:2px}

/* footer */
.foot-about{left:193px;top:3680px;width:282px;font-size:9.6px;line-height:1.6;color:#dfe2f2}
.foot-head{font-size:12px;font-weight:600;color:var(--white);letter-spacing:.3px;padding-bottom:8px;border-bottom:1px solid rgba(255,255,255,.25);width:160px}
.foot-links{font-size:11.5px;line-height:1.55;color:var(--white);margin-top:10px;list-style:none}
.news-input{left:826px;top:3661px;width:110px;height:24px;background:var(--white)}
.news-btn{left:936px;top:3661px;width:70px;height:24px;background:var(--cta);color:var(--white);font-size:10px;display:flex;align-items:center;justify-content:center}
.social{width:20px;height:20px;border:1.2px solid var(--white);border-radius:50%}
.foot-bottom{left:193px;top:3840px;width:813px;display:flex;justify-content:space-between;font-size:10.5px;color:var(--white)}
</style>
</head>
<body>

<!-- hero -->
<section class="abs hero">
  <div class="abs brand" style="left:120px;top:22px">
    <div class="brand-dot"></div>
    <div><div class="brand-name">SENTINEL</div><div class="brand-sub">Ridge Advisors</div></div>
  </div>
  <nav class="abs nav"><span>WHO WE ARE</span><span>SERVICES</span><span>NEWS</span><span>CONTACT</span></nav>
  <div class="abs btn-outline-light">CLIENT LOGIN</div>
  <div class="abs btn-cta quote-btn">GET FREE QUOTE</div>
  <h1 class="abs hero-title"><span class="l1">THE MOST EFFECTIVE</span><span class="l2">FINANCIAL PLANS</span><span class="l3">START WITH TAX PLANNING.</span></h1>
  <div class="abs btn-cta hero-learn">LEARN MORE</div>
  <div class="abs hero-photo" role="img" aria-label="Photo of hands using a calculator beside a keyboard"></div>
</section>

<!-- intro -->
<div class="abs ghost-circle" style="left:-90px;top:775px;width:180px;height:270px;border-radius:50%"></div>
<div class="abs ghost-circle" style="left:814px;top:704px;width:334px;height:334px"></div>
<h2 class="abs h2" style="left:193px;top:744px;width:380px">Few financial advisors offer tax expertise, but when they do, you benefit.</h2>
<p class="abs body" style="left:193px;top:866px;width:370px">Learn how our unique team combines financial planning, investments and smart tax and income generation strategies to help you achieve your goals faster.</p>
<div class="abs btn-outline" style="left:193px;top:957px;width:203px;height:37px">Learn why we’re different</div>

<div class="abs photo-calc" role="img" aria-label="Photo of a calculator held in hands"></div>
<h2 class="abs h2" style="left:611px;top:1160px;width:420px;font-size:22.5px;line-height:1.5">Cookie-cutter financial planning and investment can leave your future at risk. That’s why we do it differently.</h2>
<p class="abs body" style="left:611px;top:1277px;width:400px;font-size:12.5px">You need better strategies in today’s complex financial landscape. At Sentinel Ridge Advisors, we bring financial planning, investment management, retirement income, tax and estate planning expertise together under one roof. Our unique team works together to help you make the most of your resources.</p>
<div class="abs btn-solid" style="left:612px;top:1405px;width:175px;height:37px">Meet Our Specialists</div>

<!-- promise band -->
<section class="abs band"></section>
<p class="abs band-lead">Better strategies to preserve and grow wealth,</p>
<p class="abs band-strong">Generate income and reduce your taxes.</p>
<p class="abs band-note">Here’s what you can expect when you work with Sentinel.</p>
<div class="abs band-arrow">
  <svg width="34" height="28" viewBox="0 0 34 28" fill="none" stroke="#2c3794" stroke-width="2.4"><path d="M3 3l14 12 14-12"/><path d="M3 12l14 12 14-12"/></svg>
</div>

<!-- services -->
<div class="abs svc" style="left:246px;top:1974px;width:187px;height:175px">
  <svg viewBox="0 0 54 54" fill="none" stroke="#2c3794" stroke-width="1.8"><circle cx="27" cy="24" r="11"/><path d="M22 36h10M23 40h8M24 44h6"/><path d="M27 6v4M12 12l3 3M42 12l-3 3M8 24h4M46 24h-4"/><text x="27" y="28" font-size="11" text-anchor="middle" fill="#2c3794" stroke="none" font-family="Outfit">$</text></svg>
  <span>Investment<br>Management</span>
</div>
<div class="abs svc active" style="left:452px;top:2076px;width:184px;height:175px">
  <svg viewBox="0 0 54 54" fill="none" stroke="#ffffff" stroke-width="1.8"><circle cx="27" cy="12" r="8"/><path d="M27 20v12M27 26c-6 0-10-3-12-6M27 26c6 0 10-3 12-6"/><path d="M17 32h20l-3 16H20z"/><text x="27" y="16" font-size="10" text-anchor="middle" fill="#fff" stroke="none" font-family="Outfit">$</text></svg>
  <span>Retirement<br>Income Planning</span>
</div>
<div class="abs svc" style="left:246px;top:2164px;width:187px;height:175px">
  <svg viewBox="0 0 54 54" fill="none" stroke="#2c3794" stroke-width="1.8"><circle cx="30" cy="16" r="9"/><circle cx="30" cy="16" r="5"/><path d="M6 40l10-6h10c3 0 3 4 0 4h-8M26 38l14-6c3-1 5 2 2 4L26 46H6"/></svg>
  <span>Comprehensive<br>Financial Planning</span>
</div>
<div class="abs svc" style="left:452px;top:2265px;width:184px;height:175px">
  <svg viewBox="0 0 54 54" fill="none" stroke="#2c3794" stroke-width="1.8"><path d="M12 6h24v40H16c-3 0-4-2-4-4z"/><path d="M20 16h12M20 22h12M20 28h8"/><circle cx="38" cy="40" r="7"/><path d="M34 44l8-8"/><text x="16" y="20" font-size="10" fill="#2c3794" stroke="none" font-family="Outfit">$</text></svg>
  <span>Tax Planning</span>
</div>
<div class="abs svc" style="left:651px;top:2173px;width:186px;height:175px">
  <svg viewBox="0 0 54 54" fill="none" stroke="#2c3794" stroke-width="1.8"><rect x="8" y="6" width="22" height="40"/><path d="M12 20h14M12 26h14M12 32h14M12 38h10"/><rect x="28" y="20" width="18" height="26"/><path d="M31 24h12v5H31zM31 33h3M36 33h3M41 33h2M31 38h3M36 38h3M41 38h2"/><text x="12" y="15" font-size="9" fill="#2c3794" stroke="none" font-family="Outfit">%</text></svg>
  <span>Estate Planning</span>
</div>
<h2 class="abs svc-heading"><strong>Personalized<br>solutions</strong> to help<br>your money work<br>harder for you</h2>

<!-- check-up -->
<div class="abs checkup-photo" role="img" aria-label="Photo of a hand with a pen over a calculator and a rising bar chart overlay"></div>
<svg class="abs checkup-card" viewBox="0 0 427 378" preserveAspectRatio="none"><polygon points="0,0 427,30 427,350 0,378" fill="#f4f5f9"/></svg>
<h3 class="abs checkup-title">The Sentinel $549<br>Retirement Check-Up</h3>
<p class="abs checkup-text">We know it’s a big decision to hire or switch advisors. That’s why we provide an easy way to try us out. At the same time, you can get a valuable second opinion to find out if you’re on track to retire. There’s no pressure, and either way, you’ll walk away with valuable insights on what you should be doing to secure your future.</p>
<div class="abs btn-solid" style="left:258px;top:2838px;width:114px;height:33px;font-size:11.5px">Learn More</div>

<!-- contact -->
<div class="abs emblem" style="left:576px;top:3036px;width:48px;height:48px"></div>
<h2 class="abs contact-title">CONTACT</h2>
<p class="abs contact-lead">Lorem ipsum dolor sit amet, consectetur adipiscing elit<br>Nunc ac consectetur leo. Mauris aliquam.</p>

<div class="abs footer-bg" role="img" aria-label="Dark blue mountain landscape backdrop"></div>
<svg class="abs" style="left:0;top:3380px" width="1200" height="40" viewBox="0 0 1200 40" preserveAspectRatio="none"><path d="M0 40V10Q600 -6 1200 10V40z" fill="#1f2a70"/></svg>

<section class="abs form-card"></section>
<h3 class="abs form-title" style="font-weight:400">Feel Free to Contact Us</h3>
<div class="abs field" style="left:283px;top:3283px;width:310px;height:30px">First Name</div>
<div class="abs field" style="left:606px;top:3283px;width:311px;height:30px">Last Name</div>
<div class="abs field" style="left:283px;top:3327px;width:310px;height:30px">Email</div>
<div class="abs field" style="left:606px;top:3327px;width:311px;height:30px">Subject</div>
<div class="abs field" style="left:283px;top:3370px;width:634px;height:74px">Message...</div>
<div class="abs submit">SUBMIT</div>

<!-- footer -->
<div class="abs brand" style="left:193px;top:3584px">
  <div class="brand-dot" style="width:50px;height:50px"></div>
  <div><div class="brand-name" style="font-size:30px">SENTINEL</div><div class="brand-sub" style="font-size:15px">Ridge Advisors</div></div>
</div>
<p class="abs foot-about">With over 55 years of combined experience, Sentinel Ridge Advisors helps successful people more effectively prepare for the future. Our unique small team of wealth managers, financial planners and tax professionals bring you the strategies you need to preserve your wealth, minimize your taxes and create a confident retirement. While we’re based in Ashbourne County, Ohio, we serve clients nationwide.</p>
<div class="abs" style="left:576px;top:3600px">
  <div class="foot-head">SITELINKS</div>
  <ul class="foot-links"><li>Who We Are</li><li>Services</li><li>News</li><li>Sitemap</li><li>Client Login</li><li>Contact</li></ul>
</div>
<div class="abs" style="left:826px;top:3600px">
  <div class="foot-head" style="width:180px">STAY IN TOUCH</div>
  <p style="font-size:11px;color:#fff;margin-top:10px">Subscribe Our Newsletter</p>
</div>
<div class="abs news-input"></div>
<div class="abs news-btn">Subscribe</div>
<div class="abs" style="left:826px;top:3700px;display:flex;gap:5px"><span class="social"></span><span class="social"></span><span class="social"></span></div>
<div class="abs" style="left:193px;top:3825px;width:813px;height:1px;background:rgba(255,255,255,.15)"></div>
<div class="abs foot-bottom"><span>© 2021 Sentinel Ridge Advisors. All Rights Reserved.</span><span>Privacy &amp; Policy &nbsp;|&nbsp; Faq &nbsp;|&nbsp; Terms.</span></div>

</body>
</html>
```